Online Consultancy Needs a New Logo & Business Card Design

Based on the new logo we just received from another contest here on Maketrove,

You'll find a few different versions of our logo as well as examples of business card designs we like in this folder:
==> https://share.plumvault.net/folderview?id=7Kq2WzTn4pLrXcv9BsHaYe1MoD5g&usp=sharing

We are considering two options:
- clean, black design
- clean, white/blue design

We're willing to consider both options.

We're considering adding some special effects to the cards when printing - emboss, rounded corners, etc.

However, please deliver a design WITHOUT round corners.

Target Market(s)

Successful business people, serious and older audience.

Industry/Entity Type

Business

Contact Information for Business Card

For the business card, I would like a minimalistic card with the logo on one side (perhaps in the middle) and the contact information on the other.

For the contact information please use:
Name: Peter Lund
Position: Founder
Email: peter.lund@korvim.com
Phone Number: +381 63 98 76 210
Website URL: www.korvim.com

Font styles to use
Serif
Sans Serif

Requirements
Must have
• Must fit in perfectly with our current website design.

```html
<!DOCTYPE html>
<html lang="en">
<head>
<meta charset="utf-8">
<title>Korvim Business Card</title>
<link href="https://fonts.googleapis.com/css2?family=Exo+2:wght@400;500;600&display=swap" rel="stylesheet">
<style>
  :root {
    --backdrop: #cfcfcf;
    --card: #ffffff;
    --brand-blue: #1aa9e6;
    --ink: #2b2b2b;
    --ink-soft: #3a3a3a;
    --swoosh-grey: #e3e3e3;
  }
  html, body {
    margin: 0;
    width: 1200px;
    height: 900px;
    overflow: hidden;
    background: var(--backdrop);
    font-family: "Exo 2", sans-serif;
  }
  .business-card {
    position: absolute;
    left: 120px;
    top: 176px;
    width: 960px;
    height: 548px;
    background: var(--card);
    box-shadow: 0 10px 30px rgba(0,0,0,0.18);
    overflow: hidden;
  }
  .card-swoosh {
    position: absolute;
    inset: 0;
    width: 960px;
    height: 548px;
  }
  .brand-mark {
    position: absolute;
    left: 70px;
    top: 80px;
    display: flex;
    align-items: center;
    gap: 18px;
  }
  .brand-mark__dot {
    width: 34px;
    height: 34px;
    border-radius: 50%;
    background: var(--brand-blue);
  }
  .brand-mark__name {
    font-size: 96px;
    font-weight: 500;
    color: var(--brand-blue);
    letter-spacing: 2px;
    line-height: 1;
  }
  .holder {
    position: absolute;
    right: 70px;
    top: 110px;
    text-align: right;
  }
  .holder__name {
    font-size: 30px;
    font-weight: 500;
    color: var(--brand-blue);
    letter-spacing: 2px;
    text-transform: uppercase;
    margin: 0;
  }
  .holder__role {
    font-size: 21px;
    color: var(--ink);
    letter-spacing: 2px;
    text-transform: uppercase;
    margin: 4px 0 0;
  }
  .contact-list {
    position: absolute;
    left: 70px;
    top: 250px;
    margin: 0;
    padding: 0;
    list-style: none;
  }
  .contact-list li {
    display: flex;
    align-items: center;
    gap: 12px;
    font-size: 20px;
    color: var(--ink-soft);
    letter-spacing: 1px;
    height: 32px;
  }
  .contact-icon {
    width: 22px;
    height: 22px;
    flex: none;
  }
</style>
</head>
<body>
  <div class="business-card">
    <svg class="card-swoosh" viewBox="0 0 960 548" aria-hidden="true">
      <path d="M0 514 C 520 506, 790 410, 900 212 C 770 400, 500 500, 0 506 Z" fill="var(--swoosh-grey)"/>
      <path d="M0 524 C 520 516, 800 414, 960 200 L960 226 C 800 436, 520 532, 0 536 Z" fill="var(--ink)"/>
      <path d="M0 548 L0 542 C 520 538, 820 444, 960 240 L960 548 Z" fill="var(--brand-blue)"/>
    </svg>

    <div class="brand-mark">
      <span class="brand-mark__dot"></span>
      <span class="brand-mark__name">korvim</span>
    </div>

    <div class="holder">
      <p class="holder__name">Daniel Harrow</p>
      <p class="holder__role">Financial Advisor</p>
    </div>

    <ul class="contact-list">
      <li>
        <svg class="contact-icon" viewBox="0 0 22 22" aria-hidden="true"><circle cx="11" cy="11" r="11" fill="var(--brand-blue)"/><path d="M7 6 l3 0 l1 3 l-2 1 a7 7 0 0 0 3 3 l1-2 l3 1 l0 3 a9 9 0 0 1 -9 -9z" fill="#fff"/></svg>
        014 725 3860
      </li>
      <li>
        <svg class="contact-icon" viewBox="0 0 22 22" aria-hidden="true"><circle cx="11" cy="11" r="11" fill="var(--brand-blue)"/><rect x="8" y="5" width="6" height="12" rx="1" fill="none" stroke="#fff" stroke-width="1.5"/></svg>
        014 725 3860
      </li>
      <li>
        <svg class="contact-icon" viewBox="0 0 22 22" aria-hidden="true"><circle cx="11" cy="11" r="11" fill="var(--brand-blue)"/><rect x="5.5" y="7" width="11" height="8" fill="#fff"/><path d="M5.5 7 l5.5 4.5 l5.5 -4.5" fill="none" stroke="var(--brand-blue)" stroke-width="1.2"/></svg>
        yourname@mailbox.com
      </li>
      <li>
        <svg class="contact-icon" viewBox="0 0 22 22" aria-hidden="true"><circle cx="11" cy="11" r="11" fill="var(--brand-blue)"/><circle cx="11" cy="11" r="5.5" fill="none" stroke="#fff" stroke-width="1.4"/><path d="M5.5 11 h11 M11 5.5 v11" stroke="#fff" stroke-width="1.2"/></svg>
        www.yoursitename.com
      </li>
      <li>
        <svg class="contact-icon" viewBox="0 0 22 22" aria-hidden="true"><circle cx="11" cy="11" r="11" fill="var(--brand-blue)"/><path d="M11 17 C 7 12, 7 10, 7 9 a4 4 0 0 1 8 0 c0 1, 0 3, -4 8z" fill="#fff"/><circle cx="11" cy="9" r="1.5" fill="var(--brand-blue)"/></svg>
        047.12th floor.Grove Harbor Road LKG
      </li>
    </ul>
  </div>
</body>
</html>
```